Business Card design for new private practice opening

I need a business card design for my new private practice with my new logo uploaded as a file
On the front the logo
On the back: maybe a small logo somewhere?
Priv. Doz. DDr. Corinna Vestaluk
Fachärztin für Allgemein- & Viszeralchirurgie
Address: xxx
Tel: xxx
Mobil:xxx
Webseite:xxx
Email:xxx

Contact Information for Business Card

See project description above for details

Requirements
Nice to have
• I would like the colors of the logo incorporated into the business card

```html
<!DOCTYPE html>
<html lang="de">
<head>
<meta charset="utf-8">
<title>Auental Chirurgie – Visitenkarte</title>
<link rel="stylesheet" href="https://fonts.googleapis.com/css2?family=Montserrat:wght@400;500;600;700&display=swap">
<style>
  :root {
    --backdrop: #262626;
    --card-dark: #262626;
    --card-edge: #1f1f1f;
    --teal: #3aa5a1;
    --teal-light: #4db8b2;
    --grey: #8a8a8a;
    --grey-light: #a3a3a3;
    --white: #ffffff;
  }
  * { box-sizing: border-box; margin: 0; padding: 0; }
  html, body { width: 1200px; height: 576px; overflow: hidden; background: var(--backdrop); }
  body { font-family: "Montserrat", sans-serif; position: relative; }

  .card {
    position: absolute;
    top: 138px;
    background: var(--card-dark);
    border-radius: 8px;
    overflow: hidden;
    box-shadow: 0 2px 10px rgba(0,0,0,.45);
  }

  /* Front */
  .card--front { left: 102px; width: 484px; height: 294px; }
  .front__mark {
    position: absolute; left: 168px; top: 46px;
    width: 148px; height: 148px; border-radius: 50%;
    border: 5px solid #1c1c1c;
    background: #2c2c2c;
  }
  .front__name {
    position: absolute; left: 0; right: 0; top: 200px;
    text-align: center; font-weight: 700; font-size: 24px;
    color: var(--teal); letter-spacing: .2px;
  }
  .front__web {
    position: absolute; left: 0; right: 0; top: 228px;
    text-align: center; font-size: 12px; letter-spacing: 2.6px;
    color: var(--grey);
  }
  .front__band {
    position: absolute; left: 0; right: 0; bottom: 0; height: 10px;
    background: var(--teal);
  }

  /* Back */
  .card--back { left: 596px; width: 480px; height: 292px; }
  .back__waves { position: absolute; inset: 0; }
  .back__title {
    position: absolute; left: 18px; top: 20px; color: var(--white);
  }
  .back__name { font-weight: 600; font-size: 18px; line-height: 22px; }
  .back__specialty { font-size: 11.5px; line-height: 17px; margin-top: 3px; padding-left: 2px; }

  .back__brand { position: absolute; left: 244px; top: 112px; display: flex; align-items: center; gap: 10px; }
  .back__mark { width: 60px; height: 60px; border-radius: 50%; border: 3px solid var(--grey); }
  .back__brandname {
    font-weight: 600; font-size: 24px; line-height: 29px; color: var(--grey-light);
  }

  .back__contacts { position: absolute; left: 20px; top: 199px; list-style: none; }
  .back__contacts li {
    display: flex; align-items: center; gap: 9px;
    font-size: 13px; line-height: 18.5px; color: var(--grey-light);
  }
  .back__contacts svg { width: 10px; height: 10px; fill: var(--teal); flex: none; }

  .back__address {
    position: absolute; right: 19px; top: 217px; text-align: right;
    font-size: 13px; line-height: 18px; color: var(--grey); font-style: normal;
  }
</style>
</head>
<body>

<section class="card card--front" aria-label="Vorderseite">
  <div class="front__mark"></div>
  <p class="front__name">AUENTAL CHIRURGIE</p>
  <p class="front__web">www.auentalchirurgie.com</p>
  <div class="front__band"></div>
</section>

<section class="card card--back" aria-label="Rückseite">
  <svg class="back__waves" viewBox="0 0 480 292" preserveAspectRatio="none" aria-hidden="true">
    <path d="M0,0 H480 V66 C400,40 320,34 240,60 C160,88 90,126 0,124 Z" fill="var(--teal)"/>
    <path d="M0,124 C90,126 160,88 240,60 C320,34 400,40 480,66 V80 C400,56 320,52 240,76 C160,100 90,140 0,146 Z" fill="#1e1e1e"/>
    <path d="M0,138 C90,136 160,98 240,72 C300,54 360,52 420,58 C380,58 320,64 250,86 C170,112 90,150 0,152 Z" fill="var(--grey)"/>
    <path d="M300,62 C360,50 420,52 480,72 V88 C430,66 370,58 300,62 Z" fill="var(--grey)"/>
  </svg>

  <div class="back__title">
    <h1 class="back__name">Priv. Doz. DDr.<br>Corinna Vestaluk</h1>
    <p class="back__specialty">Fachärztin für Allgemein<br>- &amp; Viszeralchirurgie</p>
  </div>

  <div class="back__brand">
    <div class="back__mark"></div>
    <p class="back__brandname">AUENTAL<br>CHIRURGIE</p>
  </div>

  <ul class="back__contacts">
    <li><svg viewBox="0 0 10 10"><path d="M1 4 Q5 1 9 4 L8 5 L6.5 4.2 V3.6 H3.5 V4.2 L2 5 Z M2.5 5.5 H7.5 L8.5 9 H1.5 Z"/></svg>(000) 000-0000</li>
    <li><svg viewBox="0 0 10 10"><path d="M3 0.5 H7 V9.5 H3 Z M3.8 1.5 V7.5 H6.2 V1.5 Z"/></svg>(020) 020-22220</li>
    <li><svg viewBox="0 0 10 10"><path d="M0.5 2 H9.5 V8 H0.5 Z M1.5 3 L5 5.6 L8.5 3 Z"/></svg>demoname@website.com</li>
    <li><svg viewBox="0 0 10 10"><circle cx="5" cy="5" r="4.5"/></svg>www.website.com</li>
  </ul>

  <address class="back__address">0000 Street Name<br>Building No. 0,<br>Country - 001122</address>
</section>

</body>
</html>
```